Business Cards and Letterhead
for Modern Boston Law Firm
Simple
Gerald Dunmore
71 Ashworth Street
5th Floor
Boston, Massachusetts 02108
ger@dunmorekp-example.com
www.dunmorekp-example.com

```html
<!DOCTYPE html>
<html lang="en">
<head>
<meta charset="utf-8">
<title>Dunmore Law Group – Stationery</title>
<link href="https://fonts.googleapis.com/css2?family=Cinzel:wght@600&family=Open+Sans:wght@400;600&display=swap" rel="stylesheet">
<style>
  :root{
    --backdrop:#3b3532;
    --paper:#ffffff;
    --paper-shade:#f1f1f1;
    --brand-red:#a3171f;
    --brand-red-dark:#7c0f15;
    --steel:#8f9296;
    --steel-light:#c9cbcd;
    --ink:#5a5a5a;
    --label:#d9d3cf;
  }
  *{box-sizing:border-box;margin:0;padding:0}
  html,body{width:1200px;height:466px;overflow:hidden;background:var(--backdrop)}
  body{position:relative;font-family:"Open Sans",Arial,sans-serif;color:var(--ink)}

  .sheet{position:absolute;background:var(--paper);overflow:hidden;box-shadow:0 2px 6px rgba(0,0,0,.35)}
  .swoosh{position:absolute;left:0;bottom:0;width:100%}

  .brand{position:absolute;display:flex;align-items:center;gap:4px;white-space:nowrap}
  .brand-dot{border-radius:50%;background:var(--brand-red);flex:none}
  .brand-name{font-family:"Cinzel",Georgia,serif;font-weight:600;color:var(--brand-red);line-height:1;letter-spacing:.5px}
  .brand-sub{display:block;font-size:.42em;letter-spacing:1.5px}

  .contact{position:absolute;font-size:3.2px;line-height:4.6px;color:var(--ink);white-space:nowrap}

  .label{position:absolute;font-size:5px;letter-spacing:1.2px;text-transform:uppercase;color:var(--label);white-space:nowrap}

  /* business cards */
  .card{width:92px;height:55px}
  .card-front{left:8px;top:205px}
  .card-back{left:8px;top:272px;background:var(--brand-red)}
  .card-back .brand-name{color:var(--paper)}
  .card-back .brand-dot{background:var(--paper)}

  /* letterheads */
  .letterhead{top:15px;width:225px;height:437px}
  .letterhead-one{left:133px}
  .letterhead-two{left:395px}
  .watermark{position:absolute;left:62px;top:150px;width:100px;height:100px;border-radius:50%;background:var(--brand-red);opacity:.08}

  /* envelopes */
  .envelope{left:672px;width:518px}
  .envelope-back{top:18px;height:128px}
  .envelope-window{top:152px;height:92px;background:var(--paper-shade)}
  .envelope-front{top:256px;height:186px}
  .window{position:absolute;left:40px;top:40px;width:190px;height:34px;border:1px solid var(--steel-light);background:#fafafa}
</style>
</head>
<body>

  <p class="label" style="left:8px;top:190px">Stationery Concepts</p>

  <!-- business card front -->
  <div class="sheet card card-front">
    <div class="brand" style="left:12px;top:11px">
      <span class="brand-dot" style="width:8px;height:8px"></span>
      <span class="brand-name" style="font-size:9px">DUNMORE<span class="brand-sub">Law Group</span></span>
    </div>
    <p class="contact" style="left:12px;top:28px;font-size:3px;line-height:4px">Gerald Dunmore<br>71 Ashworth Street, 5th Floor</p>
    <svg class="swoosh" viewBox="0 0 92 20" height="20" aria-hidden="true">
      <path d="M0 16 C30 20 62 16 92 4 L92 20 L0 20Z" fill="var(--brand-red)"/>
    </svg>
  </div>
  <p class="label" style="left:30px;top:263px;font-size:4px">Business Card Front</p>

  <!-- business card back -->
  <div class="sheet card card-back">
    <div class="brand" style="left:13px;top:19px">
      <span class="brand-dot" style="width:9px;height:9px"></span>
      <span class="brand-name" style="font-size:9px">DUNMORE<span class="brand-sub">Law Group</span></span>
    </div>
  </div>
  <p class="label" style="left:30px;top:330px;font-size:4px">Business Card Back</p>

  <!-- letterhead option 1 -->
  <div class="sheet letterhead letterhead-one">
    <div class="brand" style="left:30px;top:28px">
      <span class="brand-dot" style="width:13px;height:13px"></span>
      <span class="brand-name" style="font-size:12px">DUNMORE<span class="brand-sub">Law Group</span></span>
    </div>
    <p class="contact" style="left:142px;top:28px">71 Ashworth Street, 5th Floor<br>Boston, Massachusetts 02108<br>ger@dunmorekp-example.com<br>www.dunmorekp-example.com</p>
    <div class="watermark" role="img" aria-label="Faint brand circle"></div>
    <svg class="swoosh" viewBox="0 0 225 90" height="90" aria-hidden="true">
      <path d="M0 40 C70 78 150 70 225 18" fill="none" stroke="var(--steel-light)" stroke-width="1.5"/>
      <path d="M0 52 C70 88 150 80 225 28 L225 90 L0 90Z" fill="var(--brand-red)"/>
    </svg>
  </div>
  <p class="label" style="left:216px;top:455px">Letterhead Option 1</p>

  <!-- letterhead option 2 -->
  <div class="sheet letterhead letterhead-two">
    <div class="brand" style="left:34px;top:28px">
      <span class="brand-dot" style="width:13px;height:13px"></span>
      <span class="brand-name" style="font-size:12px">DUNMORE<span class="brand-sub">Law Group</span></span>
    </div>
    <p class="contact" style="left:34px;top:52px">71 Ashworth Street, 5th Floor<br>Boston, Massachusetts 02108</p>
    <div class="watermark" role="img" aria-label="Faint brand circle"></div>
    <svg class="swoosh" viewBox="0 0 225 80" height="80" aria-hidden="true">
      <path d="M0 58 C80 76 160 60 225 22" fill="none" stroke="var(--steel-light)" stroke-width="1.5"/>
      <path d="M0 66 C80 84 160 68 225 32 L225 80 L0 80Z" fill="var(--brand-red)"/>
    </svg>
  </div>
  <p class="label" style="left:478px;top:455px">Letterhead Option 2</p>

  <!-- envelope back -->
  <div class="sheet envelope envelope-back">
    <svg width="518" height="128" aria-hidden="true">
      <defs>
        <linearGradient id="flap" x1="0" y1="0" x2="0" y2="1">
          <stop offset="0" stop-color="#6f7276"/>
          <stop offset="1" stop-color="#b9bbbe"/>
        </linearGradient>
      </defs>
      <path d="M0 0 H518 L300 100 Q259 118 218 100 Z" fill="url(#flap)"/>
      <circle cx="259" cy="104" r="12" fill="var(--brand-red)"/>
    </svg>
  </div>

  <!-- window envelope -->
  <div class="sheet envelope envelope-window">
    <svg width="518" height="92" aria-hidden="true" style="position:absolute;left:0;top:0">
      <path d="M0 0 L259 60 L518 0" fill="none" stroke="var(--steel-light)" stroke-width="1"/>
      <path d="M0 92 L200 50 M518 92 L318 50" fill="none" stroke="var(--steel-light)" stroke-width="1"/>
    </svg>
    <div class="window"></div>
  </div>

  <!-- envelope front -->
  <div class="sheet envelope envelope-front">
    <div class="brand" style="left:22px;top:18px">
      <span class="brand-dot" style="width:13px;height:13px"></span>
      <span class="brand-name" style="font-size:13px">DUNMORE<span class="brand-sub">Law Group</span></span>
    </div>
    <p class="contact" style="left:22px;top:42px;font-size:3.6px;line-height:5px">71 Ashworth Street, 5th Floor<br>Boston, Massachusetts 02108</p>
    <svg class="swoosh" viewBox="0 0 518 60" height="60" aria-hidden="true" preserveAspectRatio="none">
      <path d="M0 30 C180 58 360 46 518 8" fill="none" stroke="var(--steel-light)" stroke-width="1.5"/>
      <path d="M0 40 C180 66 360 54 518 18 L518 60 L0 60Z" fill="var(--brand-red)"/>
    </svg>
  </div>

</body>
</html>
```